Flyer Design Project

I require a double sided flyer in PSD format.
The flyer should look fresh and clean.
The flyer is for an digital marketing company that offers various services. The services are broken down into 3 main categories and the design should reflect this.
All the content is provided in the attached file
Industry/Entity Type
Digital
Requirements
Must have
- Front of the leaflet to be mainly white background with appealing text based questions in the colours in large font with relevant images.
Back if the
3 separate boxes using the colours indicated in the attachment for the services on back of the leafet.
Should not have
- Gradients
Borders on the edges of the design
Vignettes
Black elements
Any text below 10pt
Fancy fonts
Do not use old-style fonts

```html
<!DOCTYPE html>
<html lang="en">
<head>
<meta charset="utf-8">
<title>Novara – Services Flyer (Back)</title>
<link rel="stylesheet" href="https://fonts.googleapis.com/css2?family=Open+Sans:wght@400;600;700&family=Arimo:wght@700&display=swap">
<style>
  :root {
    --page-bg: #efeae2;
    --paper: #ffffff;
    --navy: #1b5b80;
    --navy-head: #236a92;
    --stripe: #4d8fb4;
    --band: #336f93;
    --green: #9fe03a;
    --sky: #8ad6f3;
    --orange: #f6931f;
    --coupon-ink: #175578;
    --coupon-grey: #9a9a9a;
    --white: #ffffff;
  }
  * { box-sizing: border-box; margin: 0; padding: 0; }
  html, body { width: 1200px; height: 1000px; overflow: hidden; }
  body { background: var(--page-bg); position: relative; font-family: "Open Sans", sans-serif; }

  .flyer {
    position: absolute; left: 93px; top: 126px;
    width: 1017px; height: 716px;
    background: var(--paper);
    overflow: hidden;
  }
  .top-band { position: absolute; left: 0; top: 0; width: 100%; height: 32px; background: var(--band); }
  .top-band::after { content: ""; position: absolute; left: 0; bottom: 0; width: 100%; height: 8px; background: var(--stripe); }

  .service {
    position: absolute; top: 51px; width: 298px; height: 434px;
    background: var(--navy);
  }
  .service--consulting { left: 42px; }
  .service--design { left: 359px; }
  .service--sem { left: 675px; }

  .service__head {
    position: relative; height: 120px;
    background: var(--navy-head);
    border-bottom: 4px solid var(--stripe);
    padding: 4px 0 0 20px;
  }
  .service__title { font-weight: 400; font-size: 43px; line-height: 54px; letter-spacing: -0.3px; }
  .service--consulting .service__title { color: var(--green); }
  .service--design .service__title { color: var(--sky); }
  .service--sem .service__title { color: var(--orange); }
  .service__arrow { position: absolute; right: 12px; top: 46px; width: 74px; height: 84px; }

  .service__list { list-style: none; color: var(--white); font-size: 18px; line-height: 31px; padding: 10px 0 0 29px; }
  .service--sem .service__list { line-height: 24px; padding: 6px 0 0 24px; }

  .coupon {
    position: absolute; left: 37px; bottom: 8px; width: 222px; height: 146px;
    background: var(--white); padding: 6px;
  }
  .coupon__inner {
    position: relative; width: 100%; height: 100%;
    border: 3px dashed #7e8a92;
    display: flex; flex-direction: column; justify-content: center;
    padding-left: 12px; padding-right: 30px;
    font-family: "Arimo", sans-serif; font-weight: 700; color: var(--coupon-ink);
  }
  .coupon--center .coupon__inner { align-items: center; padding-left: 6px; }
  .coupon__big { font-size: 48px; line-height: 50px; }
  .coupon__small { font-size: 20px; line-height: 26px; }
  .coupon__offer { font-size: 46px; line-height: 50px; white-space: nowrap; }
  .coupon__offer span { font-size: 15px; }
  .coupon__sub { font-size: 15px; white-space: nowrap; }
  .coupon__tag {
    position: absolute; right: 4px; top: 50%;
    writing-mode: vertical-rl; transform: translateY(-50%) rotate(180deg);
    font-family: "Arimo", sans-serif; font-size: 14px; letter-spacing: 1px; color: var(--coupon-grey);
  }

  .visual { position: absolute; }
  .visual--team { left: 82px; top: 489px; width: 236px; height: 149px;
    background: linear-gradient(180deg, #eef2f5, #d9e2ea); }
  .visual--growth { left: 367px; top: 486px; width: 372px; height: 152px;
    background: linear-gradient(90deg, #e6e6e6, #c9ccd0 55%, #f0e3d6); }

  .brand {
    position: absolute; left: 772px; top: 540px;
    display: flex; align-items: center; gap: 12px;
  }
  .brand__mark { width: 22px; height: 22px; background: var(--navy); }
  .brand__name { font-size: 40px; font-weight: 400; line-height: 48px; color: var(--navy); }

  .footer { position: absolute; left: 0; bottom: 0; width: 100%; height: 78px; background: var(--band); color: var(--white); }
  .footer::before { content: ""; position: absolute; left: 0; top: 0; width: 100%; height: 8px; background: var(--stripe); }
  .footer__contact { position: absolute; left: 25px; top: 20px; font-size: 14px; font-weight: 600; line-height: 22px; }
  .footer__cta { position: absolute; right: 18px; top: 28px; font-size: 15px; font-weight: 600; }
  .footer__cta strong { font-size: 23px; font-weight: 700; }
  .footer__phone { font-size: 24px; font-weight: 400; margin-left: 6px; letter-spacing: 0.5px; }
</style>
</head>
<body>
<main class="flyer">
  <div class="top-band"></div>

  <section class="service service--consulting">
    <header class="service__head">
      <h2 class="service__title">Consulting<br>Services</h2>
      <svg class="service__arrow" viewBox="0 0 74 84" aria-hidden="true">
        <path d="M6 20 Q10 4 30 6 Q52 10 54 40 L68 40 L44 78 L20 44 L34 44 Q34 26 22 22 Q12 20 6 20 Z" fill="var(--green)" stroke="#5fae1e" stroke-width="2"/>
      </svg>
    </header>
    <ul class="service__list">
      <li>Marketing Strategy<br>and Panning,</li>
      <li>Business Branding,</li>
      <li>Competition Analysis</li>
    </ul>
    <div class="coupon">
      <div class="coupon__inner">
        <div class="coupon__big">FREE</div>
        <div class="coupon__small">Consultation</div>
        <span class="coupon__tag">COUPON</span>
      </div>
    </div>
  </section>

  <section class="service service--design">
    <header class="service__head">
      <h2 class="service__title">Design<br>Services</h2>
      <svg class="service__arrow" viewBox="0 0 74 84" aria-hidden="true">
        <path d="M6 20 Q10 4 30 6 Q52 10 54 40 L68 40 L44 78 L20 44 L34 44 Q34 26 22 22 Q12 20 6 20 Z" fill="#3cb8f0" stroke="#1b7fc4" stroke-width="2"/>
      </svg>
    </header>
    <ul class="service__list">
      <li>Web Design,</li>
      <li>Website maintenance,</li>
      <li>logo design,</li>
      <li>flyer design</li>
    </ul>
    <div class="coupon coupon--center">
      <div class="coupon__inner">
        <div class="coupon__big">FREE</div>
        <div class="coupon__small">Website</div>
        <span class="coupon__tag">COUPON</span>
      </div>
    </div>
  </section>

  <section class="service service--sem">
    <header class="service__head">
      <h2 class="service__title">SEM<br>Services</h2>
      <svg class="service__arrow" viewBox="0 0 74 84" aria-hidden="true">
        <path d="M6 20 Q10 4 30 6 Q52 10 54 40 L68 40 L44 78 L20 44 L34 44 Q34 26 22 22 Q12 20 6 20 Z" fill="#f4a466" stroke="#d9782c" stroke-width="2"/>
      </svg>
    </header>
    <ul class="service__list">
      <li>Local Business Marketing,</li>
      <li>ppc, email marketing,</li>
      <li>SEO, social media,</li>
      <li>content development,</li>
      <li>website audit,</li>
      <li>lead generation</li>
    </ul>
    <div class="coupon coupon--center">
      <div class="coupon__inner">
        <div class="coupon__offer">25%<span> OFF</span></div>
        <div class="coupon__sub">any SEM Package</div>
        <span class="coupon__tag">COUPON</span>
      </div>
    </div>
  </section>

  <div class="visual visual--team" role="img" aria-label="Illustration of two figures presenting at a whiteboard beside a laptop"></div>
  <div class="visual visual--growth" role="img" aria-label="Photo of celebrating business people in front of a rising orange growth chart"></div>

  <div class="brand">
    <span class="brand__mark"></span>
    <span class="brand__name">Novara</span>
  </div>

  <footer class="footer">
    <div class="footer__contact">
      www.novara.co.uk<br>
      Novara address : 12 Canalside Walk | Millbrook | MB1 4QT
    </div>
    <div class="footer__cta">Call for a <strong>FREE</strong> consultation <span class="footer__phone">0123 456 7890</span></div>
  </footer>
</main>
</body>
</html>
```